One label design for 3 different sizes of honey bottles

Our honey company -- Amber Hollow Apiary -- needs new product labels, integrating our new name and logo. We would like one label design that presents equally well on three different sizes of plastic honey bottles. Designs should include a front and back label.

Keep in mind that we really like our old label. Please submit designs that have a similar color and font scheme as the old label.

In the uploaded files, you will find (1) detailed content instructions for each size label (2 lb, 1 lb, 8 oz), (2) photo of three plastic bottles without labels, (3) *.ai file for the new company logo, and (4) image of old package label.

Requirements
Must have
• Same look and feel as our old label, but with our new name and logo

```html
<!DOCTYPE html>
<html lang="en">
<head>
<meta charset="utf-8">
<title>Amber Hollow Apiary – Honey Label</title>
<link rel="stylesheet" href="https://fonts.googleapis.com/css2?family=Rye&family=Source+Serif+4:wght@400;600&family=Archivo:wght@400;800&display=swap">
<style>
  :root {
    --backdrop: #f6e6f1;
    --cream: #f9f2e2;
    --ink: #35352f;
    --gold: #c9a02e;
    --gold-deep: #9c6f1c;
    --rule: #45453d;
  }
  * { box-sizing: border-box; margin: 0; padding: 0; }
  html, body { width: 1200px; height: 903px; overflow: hidden; background: var(--backdrop); }
  .canvas { position: relative; width: 1200px; height: 903px; }
  .label-shapes { position: absolute; inset: 0; }

  /* Front label */
  .tagline {
    position: absolute; left: 50px; width: 495px; top: 84px;
    text-align: center; font: 400 33px/1 "Source Serif 4", serif;
    color: var(--ink); letter-spacing: 1px; word-spacing: 4px;
  }
  .product-title {
    position: absolute; left: 16px; width: 562px; top: 176px;
    text-align: center; font: 400 146px/1 "Rye", serif;
    color: var(--ink); letter-spacing: -5px; white-space: nowrap;
  }
  .brand-name {
    position: absolute; left: 70px; width: 330px; top: 455px;
    display: flex; align-items: center; justify-content: center; gap: 10px;
    font: 600 30px/1.1 "Source Serif 4", serif; color: var(--gold);
  }
  .brand-name .dot { width: 14px; height: 14px; border-radius: 50%; background: var(--gold); flex: none; }
  .product-art {
    position: absolute; left: 118px; top: 520px; width: 415px; height: 306px;
    border-radius: 8px;
    background: radial-gradient(ellipse at 65% 55%, #c9953a 0%, #dcbd7c 45%, rgba(240,226,190,0.3) 80%);
  }
  .net-weight {
    position: absolute; left: 408px; top: 838px; white-space: nowrap;
    font: 400 19px/1 "Source Serif 4", serif; color: var(--ink);
  }

  /* Back label */
  .promise {
    position: absolute; left: 641px; width: 488px; top: 108px;
    font: 400 30px/39px "Source Serif 4", serif; color: var(--ink);
  }
  .promise span { display: block; text-align: justify; text-align-last: justify; white-space: nowrap; }
  .promise span.last { text-align-last: left; }
  .nutrition {
    position: absolute; left: 636px; top: 331px; width: 500px; height: 400px;
    border: 2px solid var(--ink); background: rgba(249,242,226,0.6);
    font: 400 17px/28px "Archivo", sans-serif; color: var(--ink);
  }
  .nutrition-title {
    background: var(--ink); color: var(--cream);
    font: 800 27px/41px "Archivo", sans-serif; padding-left: 10px; letter-spacing: 0.5px;
  }
  .nutrition-body { padding: 12px 20px 0 22px; }
  .nutrition-body p { white-space: nowrap; }
  .nutrition-body b { font-weight: 800; }
  .sugar-note {
    display: flex; gap: 6px; margin-top: 10px;
    font: 400 13.5px/16px "Archivo", sans-serif; text-align: center;
  }
  .sugar-note svg { flex: none; margin-top: 2px; }
  .infant-warning {
    position: absolute; left: 630px; width: 200px; top: 798px;
    text-align: center; font: 400 10px/12px "Source Serif 4", serif;
    text-transform: uppercase; color: var(--ink); white-space: nowrap;
  }
  .maker-address {
    position: absolute; right: 71px; top: 762px; text-align: right;
    font: 400 19px/23.5px "Source Serif 4", serif; font-style: normal; color: var(--ink);
    white-space: nowrap;
  }
  .maker-address .maker { font-weight: 600; letter-spacing: 0.5px; }
</style>
</head>
<body>
<main class="canvas">
  <svg class="label-shapes" width="1200" height="903" viewBox="0 0 1200 903" aria-hidden="true">
    <path d="M76,44 H531 A20 20 0 0 0 551 64 V886 H56 V64 A20 20 0 0 0 76 44 Z" fill="#35352f"/>
    <path d="M70,38 H525 A20 20 0 0 0 545 58 V880 H50 V58 A20 20 0 0 0 70 38 Z" fill="#f9f2e2" stroke="#c9a02e" stroke-width="1.5"/>
    <path d="M62,168 V70 A16 16 0 0 0 78 54 H517 A16 16 0 0 0 533 70 V168" fill="none" stroke="#45453d" stroke-width="1.5"/>
    <line x1="72" y1="172" x2="318" y2="172" stroke="#45453d" stroke-width="2.5"/>
    <line x1="90" y1="360" x2="200" y2="360" stroke="#45453d" stroke-width="2.5"/>
    <line x1="245" y1="360" x2="505" y2="360" stroke="#45453d" stroke-width="2.5"/>
    <path d="M633,38 H1139 A28 28 0 0 0 1167 66 V883 H605 V66 A28 28 0 0 0 633 38 Z" fill="#35352f"/>
    <path d="M639,52 H1133 A20 20 0 0 0 1153 72 V869 H619 V72 A20 20 0 0 0 639 52 Z" fill="#f9f2e2"/>
  </svg>

  <section class="front-label">
    <p class="tagline">LOCAL • PURE • RAW</p>
    <h1 class="product-title">HONEY</h1>
    <p class="brand-name"><span class="dot"></span>Amber Hollow Apiary</p>
    <div class="product-art" role="img" aria-label="Illustration of a honey dipper resting on a plate beside a honeycomb, with a bee in flight"></div>
    <p class="net-weight">2 LB (907g)</p>
  </section>

  <section class="back-label">
    <p class="promise">
      <span>Amber Hollow Apiary promises</span>
      <span>100% pure honey, never pasteur-</span>
      <span>ized, and sourced exclusively</span>
      <span>from beehives we keep near</span>
      <span class="last">Maple Fork, West Virginia”</span>
    </p>

    <div class="nutrition">
      <h2 class="nutrition-title">Nutrition Facts</h2>
      <div class="nutrition-body">
        <p>Servings : 43, <b>Serv. size: 1 Tbsp (21g),</b></p>
        <p>Amount per serving: <b>Calories 60,</b></p>
        <p><b>Total Fat</b> 0g (0% DV), Sat. Fat 0g (0% DV)</p>
        <p>Trans Fat 0g,</p>
        <p><b>Cholest.</b> 0mg (0% DV)</p>
        <p><b>Sodium</b> 0mg (0% DV),</p>
        <p><b>Total Carb.</b> 17g 0mg (6% DV),</p>
        <p>Fiber 0g (0% DV), Total Sugar 17g ( &nbsp;&nbsp;&nbsp;, 34% DV,</p>
        <p><b>Protein</b> 0g, Vit. D (0% DV), Calcium (0% DV),</p>
        <p>Iron (0% DV), Potas. (0% DV).</p>
        <div class="sugar-note">
          <svg width="14" height="30" viewBox="0 0 14 30" aria-hidden="true"><path d="M7,30 V6 M1,10 L7,2 L13,10" fill="none" stroke="#35352f" stroke-width="2.2"/></svg>
          <span>One serving adds 17g of sugar to your diet and represents 34% of the Daily Value for Added Sugars.</span>
        </div>
      </div>
    </div>

    <p class="infant-warning">“Do not feed honey to<br>infants under one year old”</p>
    <address class="maker-address">
      <span class="maker">AMBER HOLLOW APIARY</span><br>
      87 Linden Ridge Road<br>
      Maple Fork, WV 25999<br>
      www.amberhollowapiary.com
    </address>
  </section>
</main>
</body>
</html>
```